Business Card Design

Please copy the format of the attached card.

FRONT:
White text small blue horses head logo where "mirano" in in example

BACK:
Blue background w/ white horses head

Industry/Entity Type

Business

Contact Information for Business Card

Dalton Greer
Chief Executive Officer
Tarnwick Inns & Resorts
417 Fenmore Street | San Francisco, California 94632
Tel: +1.310.555.0184
email: dalton@tarnwickinns-example.com

```html
<!DOCTYPE html>
<html lang="en">
<head>
<meta charset="utf-8">
<title>Dalton Greer — Tarnwick Inns &amp; Resorts</title>
<link rel="stylesheet" href="https://fonts.googleapis.com/css2?family=Arimo:wght@400&display=swap">
<style>
  :root {
    --brand-blue: #1f3f7a;
    --ink: #333333;
    --paper: #ffffff;
  }
  * { margin: 0; padding: 0; box-sizing: border-box; }
  html, body {
    width: 1200px;
    height: 741px;
    overflow: hidden;
    background: var(--paper);
  }
  .card {
    position: relative;
    width: 1200px;
    height: 741px;
    background: var(--paper);
    font-family: "Arimo", Arial, sans-serif;
    color: var(--ink);
  }
  .brand-mark {
    position: absolute;
    left: 122px;
    top: 198px;
    display: flex;
    align-items: center;
    gap: 14px;
    color: var(--brand-blue);
    font-size: 50px;
    line-height: 1;
  }
  .brand-mark__dot {
    width: 22px;
    height: 22px;
    border-radius: 50%;
    background: var(--brand-blue);
  }
  .details {
    position: absolute;
    left: 158px;
    top: 368px;
  }
  .person {
    display: flex;
    align-items: baseline;
    white-space: nowrap;
  }
  .person__name {
    color: var(--brand-blue);
    font-size: 44px;
  }
  .person__title {
    margin-left: 10px;
    font-size: 29.5px;
  }
  .company {
    margin-top: 22px;
    font-size: 26.5px;
    line-height: 33px;
    white-space: nowrap;
  }
  .company__name { color: var(--brand-blue); }
  .contact {
    margin-top: 30px;
    font-size: 27px;
    line-height: 32px;
    white-space: nowrap;
  }
  .contact__label { color: var(--brand-blue); }
</style>
</head>
<body>
  <main class="card">
    <div class="brand-mark">
      <span class="brand-mark__dot"></span>
      <span class="brand-mark__name">Tarnwick</span>
    </div>

    <section class="details">
      <p class="person">
        <span class="person__name">Dalton Greer</span>
        <span class="person__title">| Chief Executive Officer</span>
      </p>

      <div class="company">
        <p class="company__name">Tarnwick Inns &amp; Resorts</p>
        <p class="company__address">417 Fenmore Street | San Francisco, California 94632</p>
      </div>

      <div class="contact">
        <p><span class="contact__label">tel:</span> +1.310.555.0184</p>
        <p><span class="contact__label">email:</span> dalton@tarnwickinns-example.com</p>
      </div>
    </section>
  </main>
</body>
</html>
```